QuillMark Business Cards

I need a business card designed for QuillMark. To get an idea of what we do please visit https://formvault.example/para-creadores-3

```html
<!DOCTYPE html>
<html lang="en">
<head>
<meta charset="utf-8">
<title>QuillMark Business Cards</title>
<link href="https://fonts.googleapis.com/css2?family=Montserrat:wght@300;400;500&display=swap" rel="stylesheet">
<style>
  :root {
    --backdrop: #2a2a2a;
    --card-dark-a: #1b1b1c;
    --card-dark-b: #2b2b2c;
    --card-light-a: #f4f4f4;
    --card-light-b: #dedede;
    --amber: #d4841a;
    --amber-fade: rgba(212, 132, 26, 0);
    --ink: #15161b;
    --silver: #d2d2d2;
    --muted: #a9a9a9;
    --white: #ffffff;
  }
  * { margin: 0; padding: 0; box-sizing: border-box; }
  html, body {
    width: 1200px; height: 1138px; overflow: hidden;
    background: var(--backdrop);
    font-family: "Montserrat", sans-serif;
  }
  .canvas { position: relative; width: 1200px; height: 1138px; }
  .card {
    position: absolute; border-radius: 18px; overflow: hidden;
    box-shadow: 0 6px 14px rgba(0,0,0,.45);
  }
  .card--front {
    left: 274px; top: 186px; width: 624px; height: 376px;
    background: linear-gradient(135deg, var(--card-dark-a), var(--card-dark-b));
  }
  .card--back {
    left: 276px; top: 608px; width: 618px; height: 374px;
    background: linear-gradient(180deg, var(--card-light-a), var(--card-light-b));
  }
  .wordmark {
    position: absolute; font-weight: 400; font-size: 30px;
    letter-spacing: 0.28em; line-height: 1; white-space: nowrap;
  }
  .tagline {
    position: absolute; display: flex; align-items: center;
    font-size: 9.5px; letter-spacing: 0.42em; white-space: nowrap;
  }
  .tagline .rule { display: block; height: 1px; margin-left: 2px; }

  .card--front .wordmark { left: 42px; top: 284px; color: var(--silver); font-weight: 300; }
  .card--front .tagline { left: 43px; top: 320px; color: var(--muted); }
  .card--front .tagline .rule { width: 102px; background: var(--muted); }

  .header-band {
    position: absolute; left: 0; top: 0; width: 100%; height: 150px;
    background: linear-gradient(180deg, var(--amber) 0%, var(--amber) 62%, var(--amber-fade) 100%);
  }
  .holder { position: absolute; right: 32px; top: 26px; text-align: right; color: var(--white); }
  .holder__name { font-size: 28px; font-weight: 400; letter-spacing: -0.01em; line-height: 1.1; }
  .holder__role { font-size: 16px; font-weight: 300; margin-top: 6px; }

  .card--back .wordmark { left: 122px; top: 151px; color: var(--ink); }
  .card--back .tagline { left: 123px; top: 186px; color: var(--amber); }
  .card--back .tagline .rule { width: 96px; background: #555; }

  .contacts { position: absolute; right: 32px; top: 264px; list-style: none; }
  .contacts li {
    display: flex; align-items: center; justify-content: flex-end;
    font-size: 14.5px; color: var(--ink); height: 26.5px;
  }
  .contacts svg { width: 15px; height: 15px; margin-left: 12px; fill: var(--amber); }
  .address { position: absolute; left: 34px; top: 320px; font-size: 14.5px; color: var(--ink); }
</style>
</head>
<body>
<main class="canvas">
  <section class="card card--front" aria-label="Card front">
    <div class="wordmark">QUILLMARK</div>
    <div class="tagline">DIGITAL NOTARY<span class="rule"></span></div>
  </section>

  <section class="card card--back" aria-label="Card back">
    <div class="header-band" role="img" aria-label="Amber and black wave decoration across the top of the card"></div>
    <div class="holder">
      <div class="holder__name">Dana Verholt</div>
      <div class="holder__role">President</div>
    </div>

    <div class="wordmark">QUILLMARK</div>
    <div class="tagline">DIGITAL NOTARY<span class="rule"></span></div>

    <ul class="contacts">
      <li>000-0000-0000
        <svg viewBox="0 0 16 16"><path d="M2 5c0-2 2-3 6-3s6 1 6 3v1h-3V5H5v1H2z"/><path d="M4 7h8l2 6H2z"/></svg>
      </li>
      <li>dana@quillmark.example
        <svg viewBox="0 0 16 16"><path d="M1 3h14v10H1z"/><path d="M1.5 3.5 8 9l6.5-5.5" fill="none" stroke="#fff" stroke-width="1.3"/></svg>
      </li>
      <li>www.quillmark.example
        <svg viewBox="0 0 16 16"><circle cx="8" cy="8" r="7"/><path d="M1 8h14M8 1v14M3 4h10M3 12h10" stroke="#fff" stroke-width="0.9" fill="none"/><ellipse cx="8" cy="8" rx="3" ry="7" fill="none" stroke="#fff" stroke-width="0.9"/></svg>
      </li>
    </ul>
    <div class="address">Lakeview City, US</div>
  </section>
</main>
</body>
</html>
```